Banner Ad Design Project

I need a banner design. The website is under construction at www.brightmarrow.example

Name: Bright Marrow
Tagline: Steady Sparks for crowded calendars

This is a leadership development and executive coaching site. The past site is live at www.quillstepnow.example. (so you can get a sense of the content)

The audience are (BUSY) executives, senior managers, leaders and top professionals, so the feel needs to be highly professional but also modern and fresh. I want to communicate energy but also solid and trust worthy and not too new agey. The audience are also people with strong social values who want to change things - so not too corporate (Ie suits!)

I would like the design to be floating on a white background, very clean and simple. I am attracted to reds or sunset (burn orange crimson colors.) But totally open to any color ideas.
I am giving an open brief for your ideas.
Here are the dimensions 960px wide, roughly 190px height.

Reason: The weekend might give more time to designers to get involved. Thanks Vina

Hi designers

You may not have seen the additions I gave to this brief.

The banner should not have leader out front photo's. Maybe less corporate than I initially thought. 
Not too corporate (no suits!) Please no chess pieces, jigsaw pieces, cartoon images, cliche leadership images. 
Am am trying for inspiration /inspiring whilst still being professional. Very simple and clean.
Please can the design be floating in a white background so that the web page is borderless - A bit like it is in http://palmoriskel.example/
Thank you

Target Market(s)

Senior managers, executives but people who also want to change the world!

Industry/Entity Type

Construction

Requirements
Should not have
• Should not have leader out front photo's.
Maybe less corporate than I initially thought.
Am am trying for inspiration /inspiring whilst still being professional.
Please no chess pieces, jigsaw pieces, cartoon images, cliche leadership images. Not too corporate (Ie suits!)

Thanks

```html
<!DOCTYPE html>
<html lang="en">
<head>
<meta charset="utf-8">
<title>Bright Marrow – Banner</title>
<link rel="stylesheet" href="https://fonts.googleapis.com/css2?family=Bodoni+Moda:ital,opsz,wght@0,6..96,400;1,6..96,400&display=swap">
<style>
  :root {
    --page-white: #ffffff;
    --frame-grey: #c9c9c9;
    --panel-light: #fbfbfb;
    --panel-mid: #ececec;
    --brand-red: #c8102e;
    --ink-dark: #2b2b2b;
    --rule-grey: #8f8f8f;
    --art-grey: #d9d9d9;
  }
  html, body {
    margin: 0;
    padding: 0;
    width: 1200px;
    height: 257px;
    overflow: hidden;
    background: var(--page-white);
  }
  .banner {
    position: relative;
    width: 1200px;
    height: 257px;
    background: var(--page-white);
  }
  .banner-panel {
    position: absolute;
    left: 12px;
    top: 12px;
    width: 1174px;
    height: 229px;
    border: 1px solid var(--frame-grey);
    background:
      linear-gradient(115deg, transparent 78%, rgba(255,255,255,0.7) 78.5%, rgba(255,255,255,0.7) 82%, transparent 82.5%),
      linear-gradient(115deg, transparent 85%, rgba(255,255,255,0.6) 85.5%, rgba(255,255,255,0.6) 88%, transparent 88.5%),
      linear-gradient(90deg, var(--panel-light) 0%, var(--panel-light) 35%, var(--panel-mid) 100%);
    overflow: hidden;
  }
  .hero-art {
    position: absolute;
    left: 12px;
    top: 2px;
    width: 440px;
    height: 225px;
    background: radial-gradient(ellipse at 30% 65%, rgba(215,38,46,0.35) 0%, rgba(215,38,46,0.08) 30%, transparent 55%),
                radial-gradient(ellipse at 75% 30%, var(--art-grey) 0%, rgba(217,217,217,0.4) 35%, transparent 65%),
                var(--panel-light);
  }
  .brand-name {
    position: absolute;
    left: 527px;
    top: 36px;
    margin: 0;
    font-family: "Bodoni Moda", "Didot", serif;
    font-weight: 400;
    font-size: 96px;
    line-height: 1;
    letter-spacing: -2px;
    color: var(--brand-red);
    white-space: nowrap;
    transform: scaleX(0.88);
    transform-origin: left center;
  }
  .tagline-row {
    position: absolute;
    left: 539px;
    top: 170px;
    display: flex;
    align-items: center;
    gap: 8px;
  }
  .tagline-rule {
    width: 153px;
    height: 1px;
    margin-top: 14px;
    background: var(--rule-grey);
  }
  .tagline {
    margin: 0;
    font-family: "Bodoni Moda", "Didot", serif;
    font-style: italic;
    font-size: 24px;
    line-height: 1;
    color: var(--ink-dark);
    white-space: nowrap;
  }
</style>
</head>
<body>
  <div class="banner">
    <div class="banner-panel">
      <div class="hero-art" role="img" aria-label="Illustration: a red figure walking ahead leaving red footprints, followed by a line of grey figures"></div>
      <h1 class="brand-name">Bright Marrow</h1>
      <div class="tagline-row">
        <span class="tagline-rule"></span>
        <p class="tagline">Steady Sparks for crowded calendars</p>
      </div>
    </div>
  </div>
</body>
</html>
```